Company brochure

I would like to redesign our existing brochure.
It shall be trifold brochure with more modern and better appealing design than the old one. I am uploading the old one. The new design shall have all all information repeated from old brochure. It could be more or less pictures. I will provide more pictures if required. The keep text is important, the font shall be more modern. Brochure size shall be trifoldt US Legal size paper 8.5" x 14". I will provide all pitures, logos etc in a original format after design concept will be established or before on request.

Industry/Entity Type

It Company

Font styles to use
Other font styles liked:
• calibri

Colors
0555a3
3176b5
85abd2
0692cd
33a6d7
85cae6
1ab09a
33b8a4
87cfc6

Requirements
Nice to have
• I need all information from existing brochure such as text, customer logos, professional assos. logos to be shown in a new one. Picture could be added more.
Should not have
• No changes allowed to company letterhead. Only slight modifications allowed to company logo

```html
<!DOCTYPE html>
<html lang="en">
<head>
<meta charset="utf-8">
<title>Meridian Refrigeration &amp; Air Conditioning – Trifold Brochure</title>
<link href="https://fonts.googleapis.com/css2?family=Lato:wght@400;700;900&family=Roboto+Condensed:wght@500;700&display=swap" rel="stylesheet">
<style>
:root{
  --navy:#0555a3; --blue:#3176b5; --blue-soft:#85abd2;
  --sky:#0692cd; --sky-mid:#33a6d7; --sky-soft:#85cae6;
  --teal:#1ab09a; --teal-mid:#33b8a4; --teal-soft:#87cfc6;
  --orange:#e08a22; --ink:#3a3f45; --stage:#000;
}
*{margin:0;padding:0;box-sizing:border-box}
html,body{width:982px;height:1200px;overflow:hidden;background:var(--stage)}
body{position:relative;font-family:"Lato",sans-serif;color:var(--ink)}
.sheet{position:absolute;left:103px;width:776px;height:471px;background:#fff;overflow:hidden}
.sheet--outside{top:110px}
.sheet--inside{top:619px}
.panel{position:absolute;top:0;width:259px;height:471px}
.p1{left:0}.p2{left:259px}.p3{left:518px;width:258px}
.photo{position:absolute}
.heading{position:absolute;background:var(--navy);color:#fff;font-weight:700;font-size:10.5px;line-height:12px;padding:2px 5px 2px 7px;border-left:4px solid var(--orange);box-shadow:2px 2px 0 var(--blue-soft)}
.body{position:absolute;font-size:5.6px;line-height:7.2px;color:#555}
.body p{margin-bottom:6px}
.bar{position:absolute;left:0;right:0;color:#fff;text-align:center;font-weight:700}
.soft-bg{position:absolute;inset:0 0 65px 0;background:linear-gradient(100deg,#f6f8fa,#e9eef3)}
.address{bottom:0;height:65px;background:var(--teal-mid);font-size:6px;line-height:9px;padding-top:11px}
.url{position:absolute;right:12px;top:15px;font-size:7.5px;font-weight:700;color:#555}
.title{position:absolute;left:60px;top:37px;font-family:"Roboto Condensed",sans-serif;font-weight:700;font-size:25px;line-height:27px;color:var(--teal)}
.services{position:absolute;left:58px;top:129px;list-style:none;font-family:"Roboto Condensed",sans-serif;font-weight:700;font-size:12px;line-height:16.5px;color:var(--navy)}
.services li::before{content:"❄";font-size:8px;color:var(--sky-mid);margin-right:5px}
.badges{position:absolute;left:0;right:0;top:414px;display:flex;justify-content:space-around;align-items:center;padding:0 22px}
.orange-strip{position:absolute;bottom:0;left:0;right:0;height:11px;background:var(--orange)}
.white-card{position:absolute;background:#fff}
.foot{bottom:0;height:37px;font-size:10.5px;line-height:37px}
.foot--blue{background:var(--sky)}.foot--teal{background:var(--teal-mid)}
.foot--navy{background:var(--sky);font-size:8px;line-height:9px;padding-top:9px}
.foot--navy small{display:block;font-size:6px;font-weight:400}
.companies{position:absolute;left:19px;top:238px;font-size:10px;line-height:12.5px;color:var(--blue)}
.clients{position:absolute;left:18px;top:272px;display:grid;grid-template-columns:repeat(3,72px);grid-auto-rows:22px;row-gap:18px;column-gap:4px;font-weight:900;font-size:12px;color:var(--navy);align-items:center}
.clients span{display:flex;align-items:center;gap:4px;height:22px;white-space:nowrap}
.dot{width:8px;height:8px;border-radius:50%;background:var(--sky);flex:none}
</style>
</head>
<body>

<section class="sheet sheet--outside">
  <div class="panel p1">
    <div class="soft-bg"></div>
    <div class="photo" role="img" aria-label="Helicopter lifting rooftop equipment over a city skyline" style="left:0;top:33px;width:96px;height:170px;background:linear-gradient(180deg,#cfe1ef,#8fb2cf 70%,#6a7f92)"></div>
    <div class="heading" style="left:107px;top:31px;width:129px">Refrigeration Facilities<br>Serviced</div>
    <div class="body" style="left:117px;top:68px;width:132px">Food processing, cold storages and distribution facilities, meat and poultry processing plants, bakeries, dairies, beverage bottling facilities, ice production, chemical plants, refineries and ice rinks.</div>
    <div class="heading" style="left:107px;top:128px;width:132px">Industrial &amp; Commercial<br>HVAC Facilities Serviced</div>
    <div class="body" style="left:117px;top:165px;width:132px">Production plant and manufacturing facilities, distribution and storage warehouses, office buildings, data centers, hospitals, colleges, shopping malls and country clubs.</div>
    <div class="heading" style="left:21px;top:249px;width:84px">Construction</div>
    <div class="body" style="left:31px;top:276px;width:96px">
      <p>Ammonia and freon refrigeration build-up systems.</p>
      <p>Refrigeration and HVAC equipment changeover.</p>
      <p>Freon packaged condensing units and chillers.</p>
      <p>Blast freezers, spiral and tunnel freezers.</p>
      <p>Computerized control, control and power wiring.</p>
    </div>
    <div class="body" style="left:134px;top:276px;width:96px">
      <p>Build-up glycol and water chillers. Air handlers and evaporators.</p>
      <p>Refrigeration, glycol, chill water and process piping.</p>
      <p>Certified X-ray quality welding.</p>
      <p>Carbon steel, stainless steel, copper, PVC and sanitary piping.</p>
      <p>Hot tapping available.</p>
    </div>
  </div>

  <div class="panel p2">
    <div class="photo" role="img" aria-label="Plate heat exchanger and piping in a plant room, tinted teal" style="left:0;top:0;width:259px;height:406px;background:linear-gradient(160deg,#5fb8a8,#2f8f85 55%,#3d9c90)"></div>
    <div class="bar address">4812 Harlow Avenue | Riverbend, CA 90210<br>P: 555-210-4400 | F: 555-210-4401<br>www.meridianrac.com<br>Lic. # 514270</div>
  </div>

  <div class="panel p3">
    <div class="url">www.meridianrac.com</div>
    <div class="photo" role="img" aria-label="Thermometer with snowflake illustration" style="left:10px;top:40px;width:40px;height:75px;background:linear-gradient(180deg,#e9eef2,#c7d2da)"></div>
    <div class="title">MERIDIAN<br>REFRIGERATION &amp;<br>AIR CONDITIONING</div>
    <ul class="services">
      <li>Industrial &amp; Commercial</li>
      <li>Ammonia &amp; Freon</li>
      <li>Service &amp; Maintenance</li>
      <li>Design &amp; Engineering</li>
      <li>Construction</li>
    </ul>
    <div class="photo" role="img" aria-label="Blue industrial compressor packages on a plant floor" style="left:0;top:219px;width:258px;height:187px;background:linear-gradient(180deg,#dfe6ee,#3f6fcf 45%,#2a4fa8 80%,#9aa3ad)"></div>
    <div class="badges">
      <svg width="44" height="34" aria-label="Professional association badge"><polygon points="11,2 33,2 43,17 33,32 11,32 1,17" fill="var(--blue)"/></svg>
      <svg width="36" height="36" aria-label="Professional association badge"><circle cx="18" cy="18" r="17" fill="var(--navy)"/></svg>
      <svg width="52" height="30" aria-label="Professional association badge"><rect x="1" y="3" width="50" height="24" fill="var(--teal)"/></svg>
    </div>
    <div class="orange-strip"></div>
  </div>
</section>

<section class="sheet sheet--inside">
  <div class="panel p1">
    <div class="photo" role="img" aria-label="Insulated ammonia pipelines with yellow labels" style="left:0;top:0;width:259px;height:434px;background:linear-gradient(180deg,#ffffff 0%,#f4f6f8 40%,#c6ced6 70%,#7f8b96)"></div>
    <div class="heading" style="left:21px;top:24px;width:66px">Experience</div>
    <div class="body" style="left:31px;top:53px;width:200px">Thirty plus years in industrial, commercial, ammonia and freon refrigeration and air conditioning. Experienced in all aspects of refrigeration projects, from design concept through execution, with the ability to cost effectively satisfy customer requirements within aggressive time frames.</div>
    <div class="white-card" style="left:86px;top:118px;width:173px;height:179px"></div>
    <div class="heading" style="left:91px;top:121px;width:145px">Major Projects Completed</div>
    <div class="body" style="left:96px;top:150px;width:150px">
      <p>675 TR, 1960 HP ammonia refrigeration system for a bakery.</p>
      <p>90 TR, 400 HP freon spiral blast freezer for meat processing plant.</p>
      <p>920 TR, 1420 HP ammonia refrigeration system for meat processing facility.</p>
      <p>1300 TR freon chiller and glycol chiller and glycol distribution system for a dairy processing plant.</p>
      <p>An ammonia refrigeration system for 560,000 sq. ft cold storage and food distribution facility.</p>
      <p>480 ton ice production facility.</p>
      <p>375 TR, 1500 HP ice-cream plant.</p>
    </div>
    <div class="bar foot foot--blue">Get A Free Quote And Survey!</div>
  </div>

  <div class="panel p2">
    <div class="heading" style="left:14px;top:24px;width:148px">Major Projects Completed</div>
    <div class="body" style="left:23px;top:53px;width:115px">
      <p>24 hour Emergency Service - Ammonia and Freon. Customized maintenance program. Troubleshooting service and repair of refrigeration and HVAC systems including all mechanical, structural, electrical and control components. Compressor rebuilding as well as vibration and oil analysis. Refrigerant conversion and recovery.</p>
      <p>Build-up ammonia and freon refrigeration systems, packaged freon refrigeration units, blast freezing/cooling systems, spiral and tunnel freezers, holding freezers and coolers, evaporators, glycol and water chillers, ice production machines, process rooms.</p>
      <p>Compressors, evaporative and air-cool condensers, recirculation packages, ammonia, water and glycol pumps, heat exchangers, control valves and regulators, electrical motors.</p>
    </div>
    <div class="body" style="left:153px;top:53px;width:92px">
      <p>Safety devices test, repair and calibration including: relief valves, leak detectors, pressure and temperature sensors, level switches and interlock devices.</p>
      <p>Packaged and split gas/electric air conditioners, heat pumps. Air handlers, exhaust fans, swamp coolers, water chillers, water towers and pumps. Exhaust and ventilation, humidification and dehumidification, clean rooms. Boilers and Boiler Piping. Refrigeration and Building Control and automation.</p>
      <p>PLC, VFD, VSD, VAV.</p>
    </div>
    <div class="photo" role="img" aria-label="Machine room with green compressor skids and yellow piping" style="left:0;top:259px;width:259px;height:175px;background:linear-gradient(180deg,#eef0f1,#c9cfcf 40%,#58706c 75%,#8f9a98)"></div>
    <div class="bar foot foot--teal">Customer Satisfaction Is Our Ultimate Goal!</div>
  </div>

  <div class="panel p3" style="background:linear-gradient(180deg,#fff 55%,#eef3f8)">
    <div class="photo" role="img" aria-label="Rooftop refrigeration units with a drafting pencil" style="left:0;top:40px;width:97px;height:94px;background:linear-gradient(180deg,#b9c7d2,#9aa5a9 60%,#6f7a7d)"></div>
    <div class="photo" role="img" aria-label="Engine room with blue compressors" style="left:0;top:141px;width:97px;height:71px;background:linear-gradient(180deg,#c9d1d6,#4f7f93 60%,#6a7880)"></div>
    <div class="heading" style="left:105px;top:24px;width:118px">Engineering Services</div>
    <div class="body" style="left:106px;top:53px;width:140px">
      <p>Design ammonia and freon systems. Buildup and packaged refrigeration systems. Liquid recirculating, flooded, and DX systems. Low and high temperature chillers. Glycol and chill water distribution systems.</p>
      <p>Energy saving and expansion projects.</p>
      <p>3D solid modeling and 2D CAD drawings. Computerized control design and implementation, PLC, VFD.</p>
      <p>Mechanical integrity surveys, safety and hazard analysis, seismic assessment. Safety programs, PSM, RMP, CalARP, MOC, SOP. Regulatory Compliance and Professional training.</p>
      <p style="font-weight:700;color:#333">Free survey and quote on your refrigeration and air conditioning equipment needs.</p>
    </div>
    <div class="companies">Companies<br>We Proudly Serve</div>
    <div class="clients">
      <span><svg width="30" height="22" aria-label="Association badge"><circle cx="15" cy="11" r="10" fill="var(--blue)"/></svg></span>
      <span>Brookvale</span><span>Harvestline</span>
      <span><i class="dot"></i>Fizzwell</span><span>Sunvale</span><span>Alpenmilk</span>
      <span><svg width="30" height="22" aria-label="Association badge"><circle cx="15" cy="11" r="10" fill="var(--blue)"/></svg></span>
      <span>Brookvale</span><span>Harvestline</span>
      <span><i class="dot"></i>Fizzwell</span><span>Sunvale</span><span>Alpenmilk</span>
    </div>
    <div class="bar foot foot--navy">MERIDIAN REFRIGERATION &amp; AIR CONDITIONING<small>555-210-4400 • www.meridianrac.com</small></div>
  </div>
</section>

</body>
</html>
```